Personal Finance e-commerce website needs a simple budget design

Hello! I am starting to sell downloadable and printable budget planners, as shown in the attached file, for people to plan ahead on their personal finances. <br/><br/>I want to see a one-page design with similar columns (for example, "Expenses, Budget, and Actual"). I would also like to see the basic formula ("Net Income = Gross income - Total Expenses") somewhere on the design. Finally, I want the design to remain mostly minimalistic and simple for the average person to plan their personal monthly budgets.<br/><br/>However, other than that, the overall design, layout, and colors will be at the graphic designer's choice. If you have any questions for me, please let me know. Thank you for your time!

Industry/Entity Type

Financial Planning

Colors

Designer to choose colors to be used in the design.

Requirements
Must have
• I want to see a one-page design with similar columns (for example, "Expenses, Budget, and Actual").
• I want the design to remain mostly minimalistic and simple for the average person to plan their personal monthly budgets.
Nice to have
• I would also like to see the basic formula ("Net Income = Gross income - Total Expenses") somewhere on the design.

```html
<!DOCTYPE html>
<html lang="en">
<head>
<meta charset="utf-8">
<title>Basic Monthly Budget</title>
<link rel="stylesheet" href="https://fonts.googleapis.com/css2?family=Bebas+Neue&family=Open+Sans:wght@400;600&display=swap">
<style>
  :root {
    --purple: #a2539f;
    --purple-dark: #7d3b7b;
    --green: #8cc63f;
    --green-dark: #6a9a2c;
    --charcoal: #4d4d4f;
    --ink: #111111;
    --muted: #8a8a8a;
    --paper: #f7f7f7;
    --row-light: #f4f4f4;
    --row-dark: #e7e7e7;
    --total-box: #a8a9ab;
    --rule: #c8c8c8;
    --white: #ffffff;
  }
  * { box-sizing: border-box; margin: 0; padding: 0; }
  html, body { width: 998px; height: 1200px; overflow: hidden; }
  body {
    background: var(--paper);
    font-family: "Open Sans", Arial, sans-serif;
    color: var(--ink);
    position: relative;
  }
  .planner { position: absolute; inset: 0; }

  .site-note {
    position: absolute; left: 0; right: 0; top: 44px;
    text-align: center;
    font-size: 17px; font-weight: 600; letter-spacing: -0.1px;
  }

  .brand {
    position: absolute; left: 60px; top: 140px;
    display: flex; align-items: center; gap: 10px;
  }
  .brand-dot {
    width: 14px; height: 14px; border-radius: 50%;
    background: var(--purple);
  }
  .brand-name {
    font-size: 19px; font-weight: 600; line-height: 1;
    color: var(--ink); white-space: nowrap;
  }

  .title {
    position: absolute; left: 282px; top: 104px;
    font-family: "Bebas Neue", Impact, sans-serif;
    font-size: 66px; font-weight: 400; line-height: 1; letter-spacing: 0.5px;
  }
  .period {
    position: absolute; left: 323px; top: 204px; width: 352px;
    border-top: 1px solid var(--rule);
    padding-top: 10px; text-align: center;
    font-size: 12px; color: var(--muted); text-transform: uppercase;
  }

  .budget-table {
    position: absolute; left: 57px; top: 283px;
    width: 885px; height: 713px;
    display: grid; grid-template-columns: repeat(3, 1fr);
    box-shadow: 0 2px 6px rgba(0,0,0,0.25);
  }
  .column {
    position: relative; display: flex; flex-direction: column;
    border-left: 1px solid #bdbdbd;
    background: var(--white);
  }
  .column:first-child { border-left: none; }
  .column-head {
    position: relative; height: 86px;
    display: flex; flex-direction: column; align-items: center; justify-content: center;
    color: var(--white);
  }
  .column-head::after {
    content: ""; position: absolute; left: 50%; bottom: -12px;
    transform: translateX(-50%);
    border-left: 13px solid transparent; border-right: 13px solid transparent;
    border-top: 12px solid var(--head);
    z-index: 2;
  }
  .column-expenses .column-head { --head: var(--purple); background: var(--purple); }
  .column-budget .column-head { --head: var(--green); background: var(--green); }
  .column-actual .column-head { --head: var(--charcoal); background: var(--charcoal); }
  .column-title {
    font-family: "Bebas Neue", Impact, sans-serif;
    font-size: 32px; line-height: 1; letter-spacing: 0.5px; margin-top: 6px;
  }
  .column-hint { font-size: 13px; margin-top: 4px; }
  .column-rows {
    height: 576px;
    background: repeating-linear-gradient(to bottom,
      var(--row-light) 0, var(--row-light) 48px,
      var(--row-dark) 48px, var(--row-dark) 96px);
  }
  .column-total { flex: 1; background: var(--row-light); position: relative; }
  .total-box {
    position: absolute; left: 46px; right: 46px; top: 10px; bottom: 0;
    background: var(--total-box);
  }

  .formula {
    position: absolute; left: 57px; top: 1027px; width: 885px; height: 90px;
  }
  .term { position: absolute; top: 6px; height: 44px; }
  .term-tag {
    height: 44px; display: flex; align-items: center; justify-content: center;
    padding-right: 12px;
    font-family: "Bebas Neue", Impact, sans-serif;
    font-size: 30px; color: var(--white); letter-spacing: 0.5px;
    clip-path: polygon(0 0, calc(100% - 14px) 0, 100% 50%, calc(100% - 14px) 100%, 0 100%);
  }
  .term::before {
    content: ""; position: absolute; left: 0; top: -8px;
    border-left: 8px solid transparent; border-bottom: 8px solid var(--fold);
  }
  .term-caption {
    margin-top: 10px; text-align: center; padding-right: 12px;
    font-size: 12px; color: var(--muted); white-space: nowrap;
  }
  .term-net { left: 0; width: 258px; --fold: var(--green-dark); }
  .term-gross { left: 315px; width: 257px; --fold: var(--green-dark); }
  .term-net .term-tag, .term-gross .term-tag { background: var(--green); }
  .term-total { left: 623px; width: 262px; --fold: var(--purple-dark); }
  .term-total .term-tag { background: var(--purple); }
  .operator {
    position: absolute; top: 2px; width: 40px; text-align: center;
    font-family: "Bebas Neue", Impact, sans-serif;
    font-size: 46px; line-height: 52px; color: var(--charcoal);
  }
  .operator-equals { left: 266px; }
  .operator-minus { left: 578px; }

  .web-pill {
    position: absolute; left: 289px; top: 1138px;
    width: 416px; height: 40px; border-radius: 20px;
    background: var(--charcoal);
    display: flex; align-items: center; justify-content: center; gap: 10px;
    color: var(--white); font-size: 21px; letter-spacing: 1px;
    box-shadow: 0 2px 4px rgba(0,0,0,0.2);
  }
  .web-pill svg { width: 22px; height: 22px; }
</style>
</head>
<body>
<main class="planner">
  <p class="site-note">Visit us at: claravance.com&nbsp; for personal financial advice!</p>

  <div class="brand">
    <span class="brand-dot"></span>
    <span class="brand-name">Clara Vance</span>
  </div>

  <h1 class="title">Basic Monthly Budget</h1>
  <p class="period">Month / Year</p>

  <section class="budget-table">
    <div class="column column-expenses">
      <header class="column-head">
        <span class="column-title">Expenses (Category)</span>
        <span class="column-hint">Custom category</span>
      </header>
      <div class="column-rows"></div>
      <div class="column-total"><span class="total-box"></span></div>
    </div>
    <div class="column column-budget">
      <header class="column-head">
        <span class="column-title">Budget (USD)</span>
        <span class="column-hint">What you plan to spend</span>
      </header>
      <div class="column-rows"></div>
      <div class="column-total"><span class="total-box"></span></div>
    </div>
    <div class="column column-actual">
      <header class="column-head">
        <span class="column-title">Actual (USD)</span>
        <span class="column-hint">What you actually spent</span>
      </header>
      <div class="column-rows"></div>
      <div class="column-total"><span class="total-box"></span></div>
    </div>
  </section>

  <section class="formula">
    <div class="term term-net">
      <div class="term-tag">Net Income</div>
      <p class="term-caption">how much money you kept</p>
    </div>
    <span class="operator operator-equals">=</span>
    <div class="term term-gross">
      <div class="term-tag">Gross Income</div>
      <p class="term-caption">how much money you earned</p>
    </div>
    <span class="operator operator-minus">-</span>
    <div class="term term-total">
      <div class="term-tag">Total Expenses</div>
      <p class="term-caption">actual expenses</p>
    </div>
  </section>

  <div class="web-pill">
    <svg viewBox="0 0 24 24" fill="none" stroke="#ffffff" stroke-width="1.8" aria-hidden="true">
      <circle cx="12" cy="12" r="10"/>
      <ellipse cx="12" cy="12" rx="4.5" ry="10"/>
      <line x1="2" y1="12" x2="22" y2="12"/>
      <path d="M4 6.5h16M4 17.5h16"/>
    </svg>
    <span>www.claravance.com</span>
  </div>
</main>
</body>
</html>
```